Family Owned Construction Company Needs Modern Business Cards

We need a new design for our business cards. We are a family owned construction company, Brantwell Construction, based in Mendon, Vermont and would like to add in our new logo and find a more modern look. We also want to use our old to make sure people know who we are. We do site development, highway, environmental, demolition, utility and aggregate.

Contact Information for Business Card

We want to have the office address, 418 Quarry Ridge Road, Harlow Falls, VT 05788 and our phone (802) 555-0137 and fax (802) 555-0164 on there as well. Our website is www.brantwellinc.example. There should be a place for the person's name, title, cell number, and email address on the card. Words that we would like to be associated with our company are honesty, predictable, reliable, integrity, dedicated, built right quality, consistent, whatever it takes, and innovation. Safety is also very important to us.

Font styles to use
Serif
Sans Serif
Other font styles liked:
• Square 721 Extented

Colors
0255a3
ffffff

Requirements
Must have
• Office address, phone number and fax number. New logo with excavator
Nice to have
• That we do site development, highway, environmental, demolition, utility, and aggregate. Both logos

```html
<!DOCTYPE html>
<html lang="en">
<head>
<meta charset="utf-8">
<title>Brantwell Construction – Business Cards</title>
<link rel="stylesheet" href="https://fonts.googleapis.com/css2?family=Open+Sans:wght@400;600;700&display=swap">
<style>
  :root {
    --navy: #2d4166;
    --ink: #141c2e;
    --white: #ffffff;
    --paper: #f7f8fa;
    --backdrop: #e6e4df;
  }
  * { box-sizing: border-box; margin: 0; padding: 0; }
  html, body {
    width: 1200px; height: 800px; overflow: hidden;
    background: var(--backdrop);
    font-family: "Open Sans", Arial, sans-serif;
  }
  .sheet {
    width: 1200px; height: 800px;
    display: flex; align-items: center; justify-content: center; gap: 40px;
  }
  .card {
    position: relative;
    width: 540px; height: 310px;
    border-radius: 18px;
    box-shadow: 0 6px 18px rgba(0,0,0,.18);
    overflow: hidden;
  }

  /* Front */
  .card--front { background: var(--navy); color: var(--white); }
  .front-brand {
    position: absolute; left: 60px; top: 92px;
    display: flex; align-items: center; gap: 18px;
  }
  .front-brand__mark { width: 64px; height: 64px; background: var(--white); flex: none; }
  .front-brand__name {
    font-weight: 600; font-size: 26px; line-height: 1.15; letter-spacing: 1px;
    text-transform: uppercase; color: var(--white);
  }
  .front-web {
    position: absolute; left: 142px; top: 190px;
    font-size: 13px; color: var(--white);
  }
  .front-services {
    position: absolute; left: 0; right: 0; bottom: 28px;
    text-align: center; font-size: 12.5px; letter-spacing: .2px; color: var(--white);
  }

  /* Back */
  .card--back { background: var(--paper); color: var(--ink); }
  .back-brand {
    position: absolute; right: 34px; top: 38px;
    display: flex; align-items: center; gap: 10px;
  }
  .back-brand__mark { width: 18px; height: 18px; background: var(--navy); flex: none; }
  .back-brand__name {
    font-weight: 700; font-size: 19px; letter-spacing: .5px;
    text-transform: uppercase; color: var(--navy);
  }
  .person {
    position: absolute; left: 34px; top: 108px;
    padding-left: 14px;
    border-left: 8px solid var(--navy);
  }
  .person__name { font-size: 22px; font-weight: 700; color: var(--ink); line-height: 1.1; }
  .person__title { font-size: 15px; font-weight: 600; color: var(--navy); }
  .contacts {
    position: absolute; left: 40px; top: 176px;
    list-style: none; font-size: 12.5px; font-weight: 600; color: var(--ink);
  }
  .contacts li { display: flex; align-items: flex-start; gap: 12px; line-height: 1.35; margin-bottom: 2px; }
  .contacts svg { width: 13px; height: 13px; flex: none; margin-top: 2px; fill: var(--navy); }
  .back-web {
    position: absolute; right: 34px; bottom: 28px;
    font-size: 12px; font-weight: 600; color: var(--navy);
  }
</style>
</head>
<body>
<main class="sheet">
  <section class="card card--front">
    <div class="front-brand">
      <span class="front-brand__mark"></span>
      <span class="front-brand__name">Brantwell<br>Construction Inc.</span>
    </div>
    <p class="front-web">www.brantwellinc.example</p>
    <p class="front-services">Site development | Highway | Environmental | Demolition | Utility | Aggregate</p>
  </section>

  <section class="card card--back">
    <div class="back-brand">
      <span class="back-brand__mark"></span>
      <span class="back-brand__name">Brantwell Construction Inc.</span>
    </div>
    <div class="person">
      <p class="person__name">Your Name</p>
      <p class="person__title">Job Title</p>
    </div>
    <ul class="contacts">
      <li>
        <svg viewBox="0 0 12 12"><path d="M6 0a4 4 0 0 0-4 4c0 3 4 8 4 8s4-5 4-8a4 4 0 0 0-4-4zm0 5.5A1.5 1.5 0 1 1 6 2.5a1.5 1.5 0 0 1 0 3z"/></svg>
        <span>418 Quarry Ridge Road<br>Harlow Falls, VT 05788</span>
      </li>
      <li>
        <svg viewBox="0 0 12 12"><path d="M3 0h6a1 1 0 0 1 1 1v10a1 1 0 0 1-1 1H3a1 1 0 0 1-1-1V1a1 1 0 0 1 1-1zm.5 1.5v8h5v-8z"/></svg>
        <span>000 000 0000</span>
      </li>
      <li>
        <svg viewBox="0 0 12 12"><path d="M2.5 0 4.5 3 3.3 4.4a7 7 0 0 0 4.3 4.3L9 7.5l3 2-1 2C5 12 0 7 .5 1z"/></svg>
        <span>(802) 555-0137</span>
      </li>
      <li>
        <svg viewBox="0 0 12 12"><path d="M3 0h5v3H3zM1 4h10v6H9v2H3v-2H1zm3 4v3h4V8z"/></svg>
        <span>(802) 555-0164</span>
      </li>
      <li>
        <svg viewBox="0 0 12 12"><path d="M0 2h12v1L6 7 0 3zm0 2.2 6 4 6-4V10H0z"/></svg>
        <span>youremail@brantwellinc.example</span>
      </li>
    </ul>
    <p class="back-web">www.brantwellinc.example</p>
  </section>
</main>
</body>
</html>
```